ZRD Roofing Billboard Design

Looking for a fresh new billboard design with my new headshot photo and using some info from my previous billboard and maybe website for design/content inspiration. My website is https://zrdroofing.com/

Also attached are my logo and current lawn sign design. I am looking for something simple, clean and modern. The landing page website should be 3816tops.com like my previous billboard has.

```html
<!DOCTYPE html>
<html lang="en">
<head>
<meta charset="utf-8">
<title>ZRD Roofing Billboard</title>
<link rel="stylesheet" href="https://fonts.googleapis.com/css2?family=Montserrat:ital,wght@0,600;0,700;0,800;1,900&display=swap">
<style>
  :root {
    --navy: #22405f;
    --navy-deep: #1c3049;
    --lime: #bfd639;
    --sky: #3ab6e6;
    --roof-blue: #3f87b4;
    --shirt: #d5dcef;
    --white: #ffffff;
  }
  * { margin: 0; padding: 0; box-sizing: border-box; }
  html, body { width: 1200px; height: 353px; overflow: hidden; background: var(--white); }
  .billboard {
    position: relative;
    width: 1200px;
    height: 353px;
    background: var(--navy);
    font-family: "Montserrat", sans-serif;
    overflow: hidden;
  }
  .hero-photo {
    position: absolute;
    left: 0; top: 0;
    width: 300px; height: 264px;
  }
  .headline {
    position: absolute;
    left: 298px; top: 18px;
    font-size: 86px;
    font-weight: 900;
    font-style: italic;
    color: var(--lime);
    line-height: 1;
    letter-spacing: 1px;
    white-space: nowrap;
  }
  .subhead {
    position: absolute;
    left: 296px; top: 101px;
    font-size: 46px;
    font-weight: 900;
    font-style: italic;
    color: var(--white);
    line-height: 1;
    letter-spacing: 2.7px;
    white-space: nowrap;
  }
  .brand {
    position: absolute;
    left: 422px; top: 163px;
    display: flex;
    align-items: center;
    gap: 12px;
    color: var(--white);
    font-weight: 700;
  }
  .brand-dot {
    width: 90px; height: 90px;
    border-radius: 50%;
    background: var(--lime);
  }
  .brand-name { line-height: 1; }
  .brand-name .main { display: block; font-size: 46px; letter-spacing: 0.5px; }
  .brand-name .sub { display: block; font-size: 16px; letter-spacing: 4.6px; margin-top: 5px; }
  .divider {
    position: absolute;
    left: 749px; top: 172px;
    width: 3px; height: 68px;
    background: var(--white);
  }
  .credentials {
    position: absolute;
    left: 790px; top: 179px;
    color: var(--white);
    font-weight: 600;
    font-size: 19px;
    letter-spacing: 1px;
    line-height: 1;
  }
  .rating { display: flex; align-items: center; gap: 8px; }
  .stars { display: flex; gap: 4px; }
  .stars svg { width: 20px; height: 20px; fill: var(--sky); }
  .licensed { margin-top: 12px; }
  .url-band {
    position: absolute;
    left: 0; top: 264px;
    width: 1200px; height: 89px;
    background: var(--lime);
  }
  .url {
    position: absolute;
    left: 318px; top: 2px;
    font-size: 77px;
    font-weight: 800;
    color: var(--navy-deep);
    line-height: 1.1;
    letter-spacing: 0.5px;
  }
</style>
</head>
<body>
<div class="billboard">
  <svg class="hero-photo" viewBox="0 0 300 264" role="img" aria-label="Photo placeholder: headshot of the company owner smiling in a light blue shirt, in front of a blue-tinted shingle roof">
    <defs>
      <linearGradient id="roofTone" x1="0" y1="0" x2="0.6" y2="1">
        <stop offset="0" stop-color="#3ab6e6"/>
        <stop offset="0.55" stop-color="#3f87b4"/>
        <stop offset="1" stop-color="#3a7aa6"/>
      </linearGradient>
      <radialGradient id="portraitTone" cx="0.48" cy="0.75" r="0.6">
        <stop offset="0" stop-color="#d5dcef"/>
        <stop offset="0.55" stop-color="#b9c6e0" stop-opacity="0.85"/>
        <stop offset="1" stop-color="#3f87b4" stop-opacity="0"/>
      </radialGradient>
    </defs>
    <polygon points="0,0 296,0 296,264 0,264" fill="url(#roofTone)"/>
    <polygon points="0,0 296,0 296,264 0,264" fill="url(#portraitTone)"/>
  </svg>

  <div class="headline">ROOF PROBLEMS?</div>
  <div class="subhead">FREE, NO-PRESSURE ESTIMATE</div>

  <div class="brand">
    <div class="brand-dot"></div>
    <div class="brand-name">
      <span class="main">ZRD</span>
      <span class="sub">ROOFING LLC</span>
    </div>
  </div>

  <div class="divider"></div>

  <div class="credentials">
    <div class="rating">
      <div class="stars">
        <svg viewBox="0 0 24 24"><polygon points="12,2 14.9,8.9 22,9.3 16.5,14 18.2,21 12,17.2 5.8,21 7.5,14 2,9.3 9.1,8.9"/></svg>
        <svg viewBox="0 0 24 24"><polygon points="12,2 14.9,8.9 22,9.3 16.5,14 18.2,21 12,17.2 5.8,21 7.5,14 2,9.3 9.1,8.9"/></svg>
        <svg viewBox="0 0 24 24"><polygon points="12,2 14.9,8.9 22,9.3 16.5,14 18.2,21 12,17.2 5.8,21 7.5,14 2,9.3 9.1,8.9"/></svg>
        <svg viewBox="0 0 24 24"><polygon points="12,2 14.9,8.9 22,9.3 16.5,14 18.2,21 12,17.2 5.8,21 7.5,14 2,9.3 9.1,8.9"/></svg>
        <svg viewBox="0 0 24 24"><polygon points="12,2 14.9,8.9 22,9.3 16.5,14 18.2,21 12,17.2 5.8,21 7.5,14 2,9.3 9.1,8.9"/></svg>
      </div>
      <span>5-STAR RATED</span>
    </div>
    <div class="licensed">LICENSED &amp; INSURED</div>
  </div>

  <div class="url-band">
    <div class="url">3816tops.com</div>
  </div>
</div>
</body>
</html>
```